Trading journal (Corvanta Loop)

I need a design for trading journal application.
I would like to start from dark version of the design and the main goal that it should be pretty intuitive for everyone. I am going to create the app from scratch and I don't have any logo or branding colors, so it is up to you to choose a color scheme but it is a dark mode, so one of the colors would be black obviously.
The app will be available for web PC, Android and iOS.

There is google document with the requirements.
https://files.plomivex.net/sheet/7QwZrT2kLpN9vB4xHs0Jd8YcGm3FaUe6/view?mode=open

Target Market(s)

Professional traders

Industry/Entity Type

Trading

Colors

Designer to choose colors to be used in the design.

Requirements
Must have
• Dark mode design for PC and mobile views, the design must be pretty intuitive for everyone.
Nice to have
• Tooltips for something non obvious; popovers after completing some actions

```html
<!DOCTYPE html>
<html lang="en">
<head>
<meta charset="utf-8">
<title>Corvanta Loop — Trading Journal Dashboard</title>
<link href="https://fonts.googleapis.com/css2?family=Outfit:wght@300;400;500&display=swap" rel="stylesheet">
<style>
  :root{
    --bg:#000;
    --panel:#19191b;
    --panel-2:#1d1d20;
    --field:#242428;
    --text:#ffffff;
    --muted:#8a8a90;
    --dim:#4a4a50;
    --accent:#2f55f0;
    --green:#22e03a;
    --red:#ff2a2a;
  }
  *{box-sizing:border-box;margin:0;padding:0}
  html,body{width:1200px;height:900px;overflow:hidden;background:var(--bg)}
  body{position:relative;font-family:'Outfit',sans-serif;color:var(--text)}
  .abs{position:absolute}

  .topbar{left:62px;top:59px;width:1054px;height:72px;background:var(--panel);border-radius:12px}
  .date-range{left:621px;top:80px;width:185px;height:31px;background:var(--field);border-radius:7px;display:flex;align-items:center;justify-content:space-between;padding:0 13px;color:var(--muted);font-size:15px}
  .divider{left:840px;top:78px;width:1px;height:36px;background:#2a2236}
  .icon-btn{top:82px;width:28px;height:28px;border-radius:50%;background:#222226;display:flex;align-items:center;justify-content:center}
  .avatar{left:1007px;top:81px;width:30px;height:30px;border-radius:50%;background:radial-gradient(circle at 50% 40%,#e0b070,#3a7a4a 70%)}
  .greet-name{left:1050px;top:89px;font-size:11px}

  .crumb{left:168px;top:174px;font-size:9.5px;color:#4b64ff}
  .import-btn{left:966px;top:150px;width:148px;height:36px;background:var(--accent);border-radius:3px;display:flex;align-items:center;justify-content:center;gap:8px;font-size:14px;font-weight:500}

  .sidebar{left:62px;top:208px;width:58px;height:590px;background:var(--panel);border-radius:12px}
  .side-active{left:63px;top:228px;width:4px;height:39px;background:var(--accent);border-radius:2px}
  .side-icon{left:77px;width:28px;height:28px}

  .welcome{left:168px;top:208px;width:215px;height:233px;border-radius:11px 11px 0 0;background:linear-gradient(180deg,#3252f0 0%,#1a2aa0 30%,#0d1250 55%,#000 100%)}
  .clock{left:237px;top:251px;font-size:26px;font-weight:300}
  .morning{left:239px;top:281px;font-size:11px;color:#b6bcd8}
  .today{left:192px;top:336px;font-size:15.5px;font-weight:500;line-height:20px}
  .synced{left:192px;top:418px;font-size:11px}

  .stat{width:214px;height:117px;border-radius:11px;padding:0 22px}
  .stat .value{position:absolute;left:23px;top:20px;font-size:33px;font-weight:400}
  .stat .label{position:absolute;left:22px;top:66px;font-size:14px}
  .stat .sub{position:absolute;left:22px;top:86px;font-size:10px;display:flex;align-items:center;gap:6px;opacity:.75}
  .stat .dot{width:12px;height:12px;border-radius:50%;background:rgba(255,255,255,.35)}
  .stat .badge{position:absolute;left:160px;top:15px;width:36px;height:36px;border-radius:50%;background:rgba(0,0,0,.35);display:flex;align-items:center;justify-content:center}
  .s-profit{left:413px;top:208px;background:linear-gradient(90deg,#ee5a66,#f5aa5c)}
  .s-win{left:656px;top:208px;background:linear-gradient(90deg,#1b8a25,#a6dc92)}
  .s-rate{left:902px;top:208px;background:linear-gradient(90deg,#0fb8cc,#95f4fa)}
  .s-fees{left:413px;top:352px;background:linear-gradient(100deg,#7a60ff,#a40ec6)}
  .s-trades{left:656px;top:352px;background:linear-gradient(110deg,#1224d8 10%,#4a8ae0 55%,#88e2e8)}
  .s-assets{left:902px;top:352px;background:linear-gradient(100deg,#f45af2,#e6acf0)}

  .chart{left:164px;top:501px;width:624px;height:297px;background:var(--panel);border-radius:12px}
  .chart-title{left:186px;top:527px;font-size:13px}
  .legend{top:529px;font-size:12px;color:#c8c8cc;display:flex;align-items:center;gap:4px}
  .legend.active{color:var(--green)}
  .ylab{right:989px;font-size:8.5px;color:#8a8a90;text-align:right}
  .xlab{top:757px;font-size:8px;color:#3a3a40}

  .coin{left:805px;width:310px;height:58px;background:var(--panel);border-radius:12px}
  .coin .mark{position:absolute;left:11px;top:8px;width:39px;height:39px;border-radius:50%}
  .coin .name{position:absolute;left:61px;top:11px;font-size:13px;font-style:italic}
  .coin .tick{position:absolute;left:61px;top:32px;font-size:10px;font-style:italic;color:var(--muted)}
  .coin svg{position:absolute;left:126px;top:10px}
  .coin .status{position:absolute;left:187px;top:13px;font-size:13px;font-style:italic}
  .coin .price{position:absolute;right:11px;top:12px;font-size:13px;font-style:italic}
  .coin .chg{position:absolute;right:13px;top:35px;font-size:8px}
  .up{color:var(--green)} .down{color:var(--red)}
</style>
</head>
<body>

<div class="abs topbar"></div>
<div class="abs date-range">Date range
  <svg width="18" height="16" viewBox="0 0 18 16" fill="none" stroke="#8a8a90" stroke-width="1.3"><path d="M1 3h16M1 8h16M1 13h16"/><circle cx="11" cy="3" r="1.8" fill="#242428"/><circle cx="6" cy="8" r="1.8" fill="#242428"/><circle cx="11" cy="13" r="1.8" fill="#242428"/></svg>
</div>
<div class="abs divider"></div>
<div class="abs icon-btn" style="left:869px"><svg width="16" height="16" viewBox="0 0 16 16" fill="none" stroke="#fff" stroke-width="1.3"><path d="M3 12l1-3 7-7 2 2-7 7-3 1zM2 15h12"/></svg></div>
<div class="abs icon-btn" style="left:916px"><svg width="16" height="16" viewBox="0 0 16 16" fill="none" stroke="#fff" stroke-width="1.2"><rect x="2" y="3" width="12" height="11" rx="2"/><path d="M5 1v3M11 1v3M2 6h12M5 9h1M8 9h1M11 9h1M5 11.5h1M8 11.5h1M11 11.5h1"/></svg></div>
<div class="abs icon-btn" style="left:961px"><svg width="16" height="16" viewBox="0 0 16 16" fill="none" stroke="#fff" stroke-width="1.2"><path d="M4 11V7a4 4 0 018 0v4l1.5 1.5h-11zM6.5 14h3"/><circle cx="12" cy="3" r="2.2" fill="#3a7bff" stroke="none"/></svg></div>
<div class="abs avatar" role="img" aria-label="User profile photo"></div>
<div class="abs greet-name">Hi Rovan!</div>

<div class="abs crumb">Dashboard ◢</div>
<div class="abs import-btn"><svg width="13" height="13" viewBox="0 0 13 13" stroke="#fff" stroke-width="1.6"><path d="M6.5 0v13M0 6.5h13"/></svg>Import Trades</div>

<div class="abs sidebar"></div>
<div class="abs side-active"></div>
<svg class="abs side-icon" style="top:233px" viewBox="0 0 28 28" fill="none" stroke="#2f55f0" stroke-width="2.4"><rect x="3" y="3" width="8" height="8" rx="2"/><rect x="17" y="3" width="8" height="8" rx="2"/><rect x="3" y="17" width="8" height="8" rx="2"/><rect x="17" y="17" width="8" height="8" rx="2"/></svg>
<svg class="abs side-icon" style="top:291px" viewBox="0 0 28 28" fill="none" stroke="#fff" stroke-width="1.6"><rect x="3" y="3" width="22" height="22" rx="6"/><path d="M8 17l4-5 4 3 4-5"/></svg>
<svg class="abs side-icon" style="top:342px" viewBox="0 0 28 28" fill="none" stroke="#fff" stroke-width="1.6"><circle cx="11" cy="16" r="8"/><circle cx="17" cy="11" r="7"/><path d="M4 4l3 0 0 3M19 22l4 0 0-3"/></svg>
<svg class="abs side-icon" style="top:393px" viewBox="0 0 28 28" fill="none" stroke="#fff" stroke-width="1.6"><ellipse cx="14" cy="14" rx="11" ry="9"/><circle cx="14" cy="14" r="4"/></svg>
<svg class="abs side-icon" style="top:443px" viewBox="0 0 28 28" fill="none" stroke="#fff" stroke-width="1.6"><path d="M3 6l7-2 4 2 4-2 7 2v17l-7-2-4 2-4-2-7 2zM14 6v17M6 10h4M6 14h4"/></svg>
<svg class="abs side-icon" style="top:494px" viewBox="0 0 28 28" fill="none" stroke="#fff" stroke-width="1.6"><circle cx="14" cy="9" r="5"/><path d="M4 25c1-6 5-8 10-8s9 2 10 8"/></svg>
<svg class="abs side-icon" style="top:545px" viewBox="0 0 28 28" fill="none" stroke="#fff" stroke-width="1.6"><rect x="3" y="5" width="22" height="19" rx="6"/><path d="M25 12h-5a3 3 0 000 6h5M9 10h6"/></svg>
<svg class="abs side-icon" style="top:595px" viewBox="0 0 28 28" fill="none" stroke="#fff" stroke-width="1.8"><rect x="4" y="5" width="20" height="19" rx="1"/><path d="M9 2v6M19 2v6M4 11h20"/></svg>
<svg class="abs side-icon" style="top:648px" viewBox="0 0 28 28" fill="none" stroke="#fff" stroke-width="1.8"><path d="M14 3l10 5.5v11L14 25 4 19.5v-11z"/><circle cx="14" cy="14" r="3.5"/></svg>
<svg class="abs side-icon" style="top:701px" viewBox="0 0 28 28" fill="none" stroke="#fff" stroke-width="1.8"><circle cx="14" cy="14" r="11"/><path d="M10.5 11a3.5 3.5 0 117 0c0 2.5-3.5 3-3.5 5.5"/><circle cx="14" cy="20" r=".8" fill="#fff"/></svg>

<div class="abs welcome"></div>
<svg class="abs" style="left:188px;top:250px" width="44" height="44" viewBox="0 0 44 44" fill="none" stroke="#fff" stroke-width="3"><circle cx="21" cy="22" r="8"/><path d="M21 4v4M21 36v4M3 22h4M35 22h4M8 9l3 3M31 32l3 3M8 35l3-3M31 12l3-3"/></svg>
<div class="abs clock">8:02:09 AM</div>
<div class="abs morning">Good Morning Rovan !</div>
<div class="abs today">Today:<br>15th January 2024</div>
<div class="abs synced">Last synced 1 minute ago !</div>

<div class="abs stat s-profit"><div class="value">$478.0</div><div class="label">Total net Profit</div><div class="sub"><span class="dot"></span>+3% Descrease than yesterday</div>
  <div class="badge"><svg width="22" height="22" viewBox="0 0 22 22" fill="none" stroke="#fff" stroke-width="1.8"><circle cx="11" cy="11" r="9"/><path d="M13.5 8c-.5-1-1.5-1.5-2.5-1.5-1.5 0-2.5.8-2.5 2s1 1.7 2.5 2 2.5.8 2.5 2-1 2-2.5 2c-1 0-2-.5-2.5-1.5M11 5v12"/></svg></div></div>
<div class="abs stat s-win"><div class="value">$507.6</div><div class="label">Average Win</div><div class="sub"><span class="dot"></span>Daily</div>
  <div class="badge"><svg width="20" height="20" viewBox="0 0 20 20" fill="none" stroke="#fff" stroke-width="1.6"><rect x="3" y="1.5" width="14" height="17" rx="2"/><path d="M6 5h8v3H6zM6 11h1M10 11h1M13 11h1M6 14h1M10 14h1M13 14h1"/></svg></div></div>
<div class="abs stat s-rate"><div class="value">79%</div><div class="label">Win Rate</div><div class="sub"><span class="dot"></span>+3% Increase than yesterday</div>
  <div class="badge"><svg width="20" height="20" viewBox="0 0 20 20" fill="none" stroke="#fff" stroke-width="1.8"><path d="M4 16L16 4"/><circle cx="5" cy="5" r="2.2"/><circle cx="15" cy="15" r="2.2"/></svg></div></div>
<div class="abs stat s-fees"><div class="value">$31.0</div><div class="label">Today Fees &amp; Commissions</div><div class="sub"><span class="dot"></span>+3% Increase than yesterday</div>
  <div class="badge"><svg width="20" height="20" viewBox="0 0 20 20" fill="none" stroke="#fff" stroke-width="1.6"><path d="M3 2v15h15M6 12l4-4 3 3 4-5"/></svg></div></div>
<div class="abs stat s-trades"><div class="value">6</div><div class="label">Trades</div><div class="sub"><span class="dot"></span>number of Ongoing Trades</div>
  <div class="badge"><svg width="20" height="20" viewBox="0 0 20 20" fill="#fff"><circle cx="12" cy="6" r="3.5"/><circle cx="6" cy="12" r="3"/><circle cx="13" cy="15" r="2.5"/></svg></div></div>
<div class="abs stat s-assets"><div class="value">$19289.1</div><div class="label">total Assets</div><div class="sub"><span class="dot"></span>wallet balance</div>
  <div class="badge"><svg width="20" height="20" viewBox="0 0 20 20" fill="none" stroke="#fff" stroke-width="1.6"><path d="M10 2l7 4v8l-7 4-7-4V6zM3 6l7 4 7-4M10 10v8"/></svg></div></div>

<div class="abs chart"></div>
<div class="abs chart-title">Profit &amp; Loss Graph</div>
<div class="abs legend active" style="left:531px"><span style="width:7px;height:7px;border-radius:50%;background:var(--green);display:inline-block;margin-right:6px"></span>Daily</div>
<div class="abs legend" style="left:590px">o Weekly</div>
<div class="abs legend" style="left:656px">o Monthly</div>
<svg class="abs" style="left:749px;top:527px" width="16" height="18" viewBox="0 0 16 18" fill="none" stroke="#fff" stroke-width="1.3"><path d="M1 3h14M1 9h14M1 15h14"/><circle cx="10" cy="3" r="2" fill="#19191b"/><circle cx="5" cy="9" r="2" fill="#19191b"/><circle cx="10" cy="15" r="2" fill="#19191b"/></svg>

<div class="abs ylab" style="top:579px">$500</div>
<div class="abs ylab" style="top:610px">$400</div>
<div class="abs ylab" style="top:641px">$300</div>
<div class="abs ylab" style="top:671px">$200</div>
<div class="abs ylab" style="top:701px">$100</div>
<div class="abs ylab" style="top:733px">0</div>

<svg class="abs" style="left:0;top:0" width="1200" height="900">
  <defs>
    <linearGradient id="area" x1="0" y1="0" x2="0" y2="1">
      <stop offset="0" stop-color="#2a3380" stop-opacity=".55"/>
      <stop offset="1" stop-color="#19191b" stop-opacity="0"/>
    </linearGradient>
  </defs>
  <g stroke="#262629" stroke-width="1">
    <path d="M224 586H763M224 615H763M224 646H763M224 676H763M224 706H763M224 739H763"/>
    <path d="M224 586V739M270 586V739M317 586V739M363 586V739M410 586V739M456 586V739M503 586V739M549 586V739M596 586V739M642 586V739M689 586V739M735 586V739"/>
  </g>
  <path d="M226 648C248 648 248 628 270 628C293 628 294 648 317 648C340 648 345 625 363 625C380 615 393 611 410 611C433 611 433 654 456 654C480 654 480 627 503 627C526 627 526 679 549 679C572 679 575 646 596 646C619 627 620 627 642 627C665 627 670 640 689 647C712 662 712 677 735 677C752 677 758 658 763 638L763 739L226 739Z" fill="url(#area)"/>
  <rect x="400" y="611" width="19" height="128" fill="#1f7a2a" opacity=".8"/>
  <path d="M226 648C248 648 248 628 270 628C293 628 294 648 317 648C340 648 345 625 363 625C380 615 393 611 410 611C433 611 433 654 456 654C480 654 480 627 503 627C526 627 526 679 549 679C572 679 575 646 596 646C619 627 620 627 642 627C665 627 670 640 689 647C712 662 712 677 735 677C752 677 758 658 763 638" fill="none" stroke="#22e03a" stroke-width="1.6"/>
  <g fill="#19191b" stroke="#22e03a" stroke-width="1">
    <circle cx="226" cy="648" r="3"/><circle cx="270" cy="628" r="3"/><circle cx="317" cy="648" r="3"/><circle cx="363" cy="625" r="3"/><circle cx="456" cy="654" r="3"/><circle cx="503" cy="627" r="3"/><circle cx="549" cy="679" r="3"/><circle cx="596" cy="646" r="3"/><circle cx="642" cy="627" r="3"/><circle cx="689" cy="647" r="3"/><circle cx="735" cy="677" r="3"/>
  </g>
  <circle cx="410" cy="611" r="5" fill="#22e03a"/><circle cx="410" cy="611" r="2" fill="#0a3a10"/>
  <text x="415" y="597" fill="#9a9aa0" font-size="11" text-anchor="middle" font-family="Outfit, sans-serif">$417</text>
</svg>

<div class="abs xlab" style="left:224px">01 Aug</div>
<div class="abs xlab" style="left:270px">02 Aug</div>
<div class="abs xlab" style="left:317px">03 Aug</div>
<div class="abs xlab" style="left:363px">04 Aug</div>
<div class="abs xlab" style="left:410px">07 Aug</div>
<div class="abs xlab" style="left:456px">08 Aug</div>
<div class="abs xlab" style="left:503px">09 Aug</div>
<div class="abs xlab" style="left:550px">10 Aug</div>
<div class="abs xlab" style="left:597px">11 Aug</div>
<div class="abs xlab" style="left:643px">14 Aug</div>
<div class="abs xlab" style="left:690px">15 Aug</div>
<div class="abs xlab" style="left:736px">16 Aug</div>

<div class="abs coin" style="top:499px"><div class="mark" style="background:#f7931a"></div><div class="name">Qorvex</div><div class="tick">QRX</div>
  <svg width="48" height="30" viewBox="0 0 48 30" fill="none" stroke="#22e03a" stroke-width="1"><path d="M0 18l4 8 4-10 3 5 4-9 3 4 3-8 2 16 3-12 3 6 3-11 3 5 4-7 3 3 3-5"/></svg>
  <div class="status up">Open</div><div class="price">$4637.99</div><div class="chg up">+9.77%</div></div>
<div class="abs coin" style="top:567px"><div class="mark" style="background:#6c7fe0"></div><div class="name">Lunetra</div><div class="tick">LNT</div>
  <svg width="48" height="30" viewBox="0 0 48 30" fill="none" stroke="#ff2a2a" stroke-width="1"><path d="M0 26l5-4 3 5 4-16 4 11 5-14 4 9 4-6 4 5 5-6 3 10"/></svg>
  <div class="status up">Open</div><div class="price">$4637.99</div><div class="chg down">-1.13%</div></div>
<div class="abs coin" style="top:636px"><div class="mark" style="background:#e8141e"></div><div class="name">Vyrex</div><div class="tick">VYX</div>
  <svg width="48" height="30" viewBox="0 0 48 30" fill="none" stroke="#ff2a2a" stroke-width="1"><path d="M0 18l5-13 4 8 5-7 3 10 5-9 3 14 4-3 3 5 5-3"/></svg>
  <div class="status down">Closed</div><div class="price">$4637.99</div><div class="chg down">-3.34%</div></div>
<div class="abs coin" style="top:705px"><div class="mark" style="background:#f7931a"></div><div class="name">Qorvex</div><div class="tick">QRX</div>
  <svg width="48" height="30" viewBox="0 0 48 30" fill="none" stroke="#22e03a" stroke-width="1"><path d="M0 18l4 8 4-10 3 5 4-9 3 4 3-8 2 16 3-12 3 6 3-11 3 5 4-7 3 3 3-5"/></svg>
  <div class="status up">Open</div><div class="price">$4637.99</div><div class="chg up">+9.77%</div></div>

<svg class="abs" style="left:961px;top:782px" width="12" height="8" viewBox="0 0 12 8" fill="none" stroke="#fff" stroke-width="1.6"><path d="M1 1l5 5 5-5"/></svg>

</body>
</html>
```